Covid 19 Exit Strategy one page brochure

I would like to design, and will need URGENT help, a brochure detailing a Covid 19 Exit Strategy plan. This brochure will need to be understood easily and the graphics inside should make it easy for people to understand without reading the entire text. This project is quite urgent and needs to be completed THIS WEEK - by Saturday may 16th at the latest. I am attaching two examples. I will provide the text.

```html
<!DOCTYPE html>
<html lang="en">
<head>
<meta charset="utf-8">
<title>COVID19 Exit Strategy Plan</title>
<link rel="stylesheet" href="https://fonts.googleapis.com/css2?family=Montserrat:wght@800;900&family=Roboto:wght@400;700&family=Roboto+Condensed:wght@700&display=swap">
<style>
  :root {
    --page: #ffffff;
    --blue-bright: #1f80de;
    --blue-mid: #14418a;
    --navy: #0b1a48;
    --ink: #05041a;
    --yellow: #f7cc1a;
    --cyan: #0aa0e2;
    --white: #ffffff;
    --dash: #1e9be6;
    --icon-fill: #1c3d7e;
  }
  * { margin: 0; padding: 0; box-sizing: border-box; }
  html, body { width: 1200px; height: 831px; overflow: hidden; background: var(--page); }
  .canvas { position: relative; width: 1200px; height: 831px; background: var(--page); }
  .brochure {
    position: absolute; left: 317px; top: 49px; width: 568px; height: 735px; overflow: hidden;
    background: linear-gradient(212deg, var(--blue-bright) 0%, var(--blue-mid) 32%, var(--navy) 62%, var(--ink) 100%);
    font-family: "Roboto", sans-serif;
  }
  .decor { position: absolute; inset: 0; width: 568px; height: 735px; }
  .headline { position: absolute; left: 0; width: 568px; text-align: center; line-height: 1; }
  .headline-kicker { top: 26px; font-family: "Roboto Condensed", sans-serif; font-weight: 700; font-size: 33px; color: var(--yellow); }
  .headline-main { top: 64px; font-family: "Montserrat", sans-serif; font-weight: 900; font-size: 54px; color: var(--white); letter-spacing: -0.5px; }
  .headline-sub { top: 113px; font-family: "Montserrat", sans-serif; font-weight: 900; font-size: 53px; color: var(--cyan); }
  .step {
    position: absolute; width: 160px; font-size: 8.6px; line-height: 10.7px; color: var(--white);
  }
  .step strong { color: var(--yellow); font-weight: 700; }
  .footer-info {
    position: absolute; left: 0; top: 691px; width: 568px; text-align: center;
    font-family: "Montserrat", sans-serif; font-weight: 800; font-size: 18px; line-height: 17px; color: var(--cyan);
  }
</style>
</head>
<body>
<div class="canvas">
  <section class="brochure">
    <svg class="decor" viewBox="0 0 568 735">
      <defs>
        <radialGradient id="iconTone" cx="50%" cy="45%" r="60%">
          <stop offset="0%" stop-color="#2a55a0" stop-opacity="0.55"/>
          <stop offset="100%" stop-color="#0f2460" stop-opacity="0.35"/>
        </radialGradient>
      </defs>

      <circle cx="463" cy="118" r="68" fill="#5b8fd6" opacity="0.45" role="img" aria-label="Large faint virus particle decoration"/>
      <circle cx="232" cy="419" r="30" fill="#4a5a8a" opacity="0.6" role="img" aria-label="Small faint virus particle decoration"/>
      <circle cx="459" cy="506" r="30" fill="#4a5f95" opacity="0.6" role="img" aria-label="Small faint virus particle decoration"/>
      <circle cx="103" cy="667" r="42" fill="#3c3a55" opacity="0.85" role="img" aria-label="Faint virus particle decoration"/>

      <g stroke="var(--dash)" stroke-width="1.1" stroke-dasharray="3 3.5">
        <line x1="284" y1="202" x2="284" y2="629"/>
        <line x1="14" y1="304" x2="552" y2="304"/>
        <line x1="14" y1="404" x2="552" y2="404"/>
        <line x1="14" y1="505" x2="552" y2="505"/>
        <line x1="14" y1="606" x2="552" y2="606"/>
      </g>

      <g fill="url(#iconTone)">
        <circle cx="56" cy="252" r="39" role="img" aria-label="Hospital building icon"/>
        <circle cx="340" cy="252" r="39" role="img" aria-label="Hospital building icon"/>
        <circle cx="56" cy="353" r="39" role="img" aria-label="Hospital building icon"/>
        <circle cx="340" cy="353" r="39" role="img" aria-label="Hospital building icon"/>
        <circle cx="56" cy="454" r="39" role="img" aria-label="Hospital building icon"/>
        <circle cx="340" cy="454" r="39" role="img" aria-label="Hospital building icon"/>
        <circle cx="56" cy="555" r="39" role="img" aria-label="Hospital building icon"/>
        <circle cx="340" cy="555" r="39" role="img" aria-label="Hospital building icon"/>
      </g>
      <g fill="none" stroke="var(--yellow)" stroke-width="1.8">
        <circle cx="56" cy="252" r="40"/><circle cx="340" cy="252" r="40"/>
        <circle cx="56" cy="353" r="40"/><circle cx="340" cy="353" r="40"/>
        <circle cx="56" cy="454" r="40"/><circle cx="340" cy="454" r="40"/>
        <circle cx="56" cy="555" r="40"/><circle cx="340" cy="555" r="40"/>
      </g>

      <path d="M54 736 L70 700 Q78 684 98 684 L470 684 Q490 684 498 700 L514 736 Z" fill="var(--white)"/>
    </svg>

    <p class="headline headline-kicker">COVID19</p>
    <h1 class="headline headline-main">EXIT STRATEGY</h1>
    <p class="headline headline-sub">PLAN</p>

    <p class="step" style="left:106px;top:231px"><strong>Lorem ipsum dolor sit amet, consectetur adipiscing elit.</strong> Sed lacinia sodales mollis. In eget mi urna. Morbi sem augue, sodales a velit ac, fermentum tincidunt augue.</p>
    <p class="step" style="left:390px;top:231px"><strong>Lorem ipsum dolor sit amet, consectetur adipiscing elit.</strong> Sed lacinia sodales mollis. In eget mi urna. Morbi sem augue, sodales a velit ac, fermentum tincidunt augue.</p>
    <p class="step" style="left:106px;top:332px"><strong>Lorem ipsum dolor sit amet, consectetur adipiscing elit.</strong> Sed lacinia sodales mollis. In eget mi urna. Morbi sem augue, sodales a velit ac, fermentum tincidunt augue.</p>
    <p class="step" style="left:390px;top:332px"><strong>Lorem ipsum dolor sit amet, consectetur adipiscing elit.</strong> Sed lacinia sodales mollis. In eget mi urna. Morbi sem augue, sodales a velit ac, fermentum tincidunt augue.</p>
    <p class="step" style="left:106px;top:433px"><strong>Lorem ipsum dolor sit amet, consectetur adipiscing elit.</strong> Sed lacinia sodales mollis. In eget mi urna. Morbi sem augue, sodales a velit ac, fermentum tincidunt augue.</p>
    <p class="step" style="left:390px;top:433px"><strong>Lorem ipsum dolor sit amet, consectetur adipiscing elit.</strong> Sed lacinia sodales mollis. In eget mi urna. Morbi sem augue, sodales a velit ac, fermentum tincidunt augue.</p>
    <p class="step" style="left:106px;top:534px"><strong>Lorem ipsum dolor sit amet, consectetur adipiscing elit.</strong> Sed lacinia sodales mollis. In eget mi urna. Morbi sem augue, sodales a velit ac, fermentum tincidunt augue.</p>
    <p class="step" style="left:390px;top:534px"><strong>Lorem ipsum dolor sit amet, consectetur adipiscing elit.</strong> Sed lacinia sodales mollis. In eget mi urna. Morbi sem augue, sodales a velit ac, fermentum tincidunt augue.</p>

    <p class="footer-info">YOUR INFO AND ADDRESS<br>HERE</p>
  </section>
</div>
</body>
</html>
```